PowerGrind Flyer

I need a flyer for a new PowerGrind gym I am starting.
I would like our logo some where on the flyer.
PowerGrind is functional movement, performed at a high intensity, that is constantly varied
PowerGrind is designed to get you in the best shape of your life no matter what your age.
The "Charter Circle" (first 40 people to signup) will receive a $30 discount for their first 3 months of PowerGrind and a Charter Tee.
Call Darrel at 555-318-2046 for details
Email us at 4570powergrind@mailnest.example
Linkwall 4570 PowerGrind Halvern
Opening December 1st
Location 417 Birchmont St
Prices starting at $79/month
Updates

the flyer will be printed on 8.5 x 11 paper and one sided

Industry/Entity Type

Gym

```html
<!DOCTYPE html>
<html lang="en">
<head>
<meta charset="utf-8">
<title>PowerGrind Flyer – Charter Circle</title>
<link rel="stylesheet" href="https://fonts.googleapis.com/css2?family=Josefin+Sans:wght@300&family=Open+Sans:wght@400;700&display=swap">
<style>
  :root {
    --frame-red: #c8090f;
    --paper: #efebee;
    --page: #ffffff;
    --ink: #111111;
    --hero-light: #e6e1e4;
    --hero-accent: #e9c9cb;
  }
  * { margin: 0; padding: 0; box-sizing: border-box; }
  html, body {
    width: 1200px;
    height: 856px;
    overflow: hidden;
    background: var(--page);
  }
  .flyer {
    position: relative;
    width: 1200px;
    height: 856px;
    background: var(--page);
  }
  .flyer__frame {
    position: absolute;
    left: 20px;
    top: 22px;
    width: 1156px;
    height: 810px;
    border: 8px solid var(--frame-red);
    background: var(--paper);
  }
  .flyer__hero {
    position: absolute;
    left: 380px;
    top: 195px;
    width: 380px;
    height: 230px;
    display: block;
  }
  .flyer__title {
    position: absolute;
    left: 166px;
    top: 472px;
    font-family: "Josefin Sans", sans-serif;
    font-weight: 300;
    font-size: 104px;
    line-height: 1;
    letter-spacing: 0.055em;
    text-transform: uppercase;
    color: var(--ink);
    white-space: nowrap;
  }
  .flyer__details {
    position: absolute;
    left: 170px;
    top: 624px;
    font-family: "Open Sans", sans-serif;
    font-size: 15.5px;
    line-height: 21.5px;
    color: var(--ink);
    list-style: none;
    white-space: nowrap;
  }
  .flyer__brand {
    position: absolute;
    left: 808px;
    top: 756px;
    display: flex;
    align-items: center;
    gap: 10px;
    font-family: "Open Sans", sans-serif;
    font-weight: 700;
    font-size: 24px;
    line-height: 1;
    color: var(--ink);
    white-space: nowrap;
  }
  .flyer__brand-mark {
    width: 18px;
    height: 18px;
    background: var(--frame-red);
  }
</style>
</head>
<body>
  <main class="flyer">
    <div class="flyer__frame"></div>

    <svg class="flyer__hero" viewBox="0 0 380 230" role="img" aria-label="Illustration of two athletes in motion inside a red swoosh">
      <defs>
        <radialGradient id="heroGlow" cx="50%" cy="50%" r="55%">
          <stop offset="0%" stop-color="var(--hero-accent)"/>
          <stop offset="100%" stop-color="var(--hero-light)"/>
        </radialGradient>
      </defs>
      <rect width="380" height="230" rx="18" fill="url(#heroGlow)"/>
    </svg>

    <h1 class="flyer__title">Charter Circle</h1>

    <ul class="flyer__details">
      <li>The "Charter Circle" (first 40 people to signup)</li>
      <li>will receive a $30 discount for their first 3 months of</li>
      <li>&nbsp;PowerGrind and a Charter Tee.</li>
      <li>Call Darrel at 555-318-2046 for details</li>
      <li>Email us at 4570powergrind@mailnest.example</li>
      <li>Linkwall 4570 PowerGrind Halvern</li>
      <li>Opening December 1st</li>
      <li>Location 417 Birchmont St</li>
      <li>Prices starting at $79/month</li>
    </ul>

    <div class="flyer__brand">
      <span class="flyer__brand-mark"></span>
      <span class="flyer__brand-name">4570 PowerGrind</span>
    </div>
  </main>
</body>
</html>
```